Building business client journey document

We want to design a journey document which helps our clients understand the process of building a house from initial conversations through to construction. I have attached an example along with the design of stages/writing we would like for ours.

```html
<!DOCTYPE html>
<html lang="en">
<head>
<meta charset="utf-8">
<title>Client Journey – Building Your Home</title>
<link href="https://fonts.googleapis.com/css2?family=PT+Sans:wght@400;700&display=swap" rel="stylesheet">
<style>
  :root{
    --sky:#5cc8d0;
    --ground:#aba87e;
    --wall:#ffffff;
    --edge:#e23a4e;
    --design:#f9c62c;
    --prelim:#2fe3c8;
    --build:#ec3462;
    --ink:#2b2b2b;
    --ink-build:#6e1630;
    --label:#111111;
    --arrow-warm:#f6b400;
    --chimney:#e9e9e9;
    --chimney-ink:#8a8a8a;
  }
  *{box-sizing:border-box;margin:0;padding:0}
  html,body{width:1200px;height:1200px;overflow:hidden;background:#fff}
  body{font-family:"PT Sans",Arial,sans-serif;color:var(--ink)}
  .stage{position:relative;width:1200px;height:1200px}
  .scene{position:absolute;left:0;top:0}

  .chimney-text{position:absolute;left:684px;top:190px;width:128px;text-align:center;
    font-size:11px;line-height:1.35;letter-spacing:.5px;color:var(--chimney-ink);text-transform:uppercase}

  .phase-title{position:absolute;white-space:nowrap;line-height:1;color:var(--ink)}
  .phase-title .big{font-size:34px}
  .phase-title .small{font-size:19px;text-transform:uppercase}
  .phase-title .over{display:block;font-size:22px;text-transform:uppercase;margin-bottom:-2px}
  .title-design{left:474px;top:208px}
  .title-prelim{left:468px;top:430px}
  .title-build{left:448px;top:812px;color:var(--ink-build)}

  .step{position:absolute;width:124px;margin-left:-62px;display:flex;flex-direction:column;align-items:center}
  .step .icon{width:82px;height:62px;border:5px solid var(--wall);border-radius:14px;
    display:flex;align-items:center;justify-content:center}
  .step .icon svg{width:42px;height:38px}
  .step .label{margin-top:-8px;background:var(--label);color:#fff;font-size:8.5px;font-weight:700;
    line-height:1.15;text-align:center;text-transform:uppercase;padding:3px 6px;min-width:62px;max-width:84px}
  .step .desc{margin-top:8px;font-size:7.6px;line-height:1.3;width:116px;color:var(--ink)}
  .col-1{left:433px}.col-2{left:580px}.col-3{left:730px}
  .row-1{top:292px}.row-2{top:488px}.row-3{top:652px}.row-4{top:872px}
</style>
</head>
<body>
<div class="stage">
  <svg class="scene" width="1200" height="1200" viewBox="0 0 1200 1200" aria-hidden="true">
    <defs>
      <clipPath id="house-inside">
        <polygon points="340,308 588,164 836,308 812,308 812,1022 340,1022"/>
      </clipPath>
      <filter id="soft-shadow" x="-10%" y="-10%" width="120%" height="120%">
        <feDropShadow dx="3" dy="4" stdDeviation="5" flood-opacity=".25"/>
      </filter>
    </defs>
    <rect class="sky" x="248" y="65" width="674" height="960" fill="var(--sky)"/>
    <rect class="ground" x="248" y="1025" width="674" height="113" fill="var(--ground)"/>

    <g class="house" filter="url(#soft-shadow)">
      <polygon points="318,316 588,148 858,316 848,322 588,160 328,322" fill="var(--wall)" stroke="var(--edge)" stroke-width="1.5"/>
      <polygon points="330,314 588,156 824,300 824,1034 330,1034" fill="var(--wall)"/>
    </g>
    <g clip-path="url(#house-inside)">
      <rect x="330" y="150" width="500" height="271" fill="var(--design)"/>
      <rect x="330" y="421" width="500" height="379" fill="var(--prelim)"/>
      <rect x="330" y="800" width="500" height="230" fill="var(--build)"/>
    </g>
    <rect class="chimney" x="678" y="158" width="138" height="104" fill="var(--chimney)" filter="url(#soft-shadow)"/>

    <g class="connectors" fill="none" stroke="var(--ink)" stroke-width="1.2" stroke-dasharray="2 3">
      <path d="M470 250 L660 250 L660 272"/>
      <path d="M430 472 L740 472 L740 482"/>
      <path d="M440 852 L745 852 L745 866"/>
    </g>

    <g class="arrows">
      <polygon points="500,318 512,323 500,328" fill="#fff"/>
      <polygon points="650,318 662,323 650,328" fill="#fff"/>
      <polygon points="500,514 512,519 500,524" fill="var(--arrow-warm)"/>
      <polygon points="650,514 662,519 650,524" fill="var(--arrow-warm)"/>
      <polygon points="796,586 806,586 801,597" fill="var(--arrow-warm)"/>
      <polygon points="662,678 650,683 662,688" fill="var(--arrow-warm)"/>
      <polygon points="512,678 500,683 512,688" fill="var(--arrow-warm)"/>
      <polygon points="500,898 512,903 500,908" fill="var(--arrow-warm)"/>
      <polygon points="650,898 662,903 650,908" fill="var(--arrow-warm)"/>
    </g>
  </svg>

  <div class="chimney-text">Hearthline logo<br>+ details</div>

  <h2 class="phase-title title-design"><span class="over">Initial</span><span class="big">Design</span><span class="small">Phase</span></h2>
  <h2 class="phase-title title-prelim"><span class="big">Preliminary</span> <span class="small">Phase</span></h2>
  <h2 class="phase-title title-build"><span class="big">Construction</span><span class="small">Stage</span></h2>

  <!-- Initial design phase -->
  <div class="step col-1 row-1">
    <div class="icon"><svg viewBox="0 0 42 38"><path d="M13 6c-3 0-6 3-5 7 2 9 9 16 18 18 4 1 7-2 7-5l-6-4-4 3c-4-2-7-5-9-9l3-4z" fill="#111"/></svg></div>
    <div class="label">Initial contact</div>
    <p class="desc">This is usually by phone or email, a quick chat with our builder, then a short questionnaire for you to fill out to see if we're a match to work together.</p>
  </div>
  <div class="step col-2 row-1">
    <div class="icon"><svg viewBox="0 0 42 38"><path d="M3 16l8-6 8 3 6-3 14 6-4 4-8 8c-2 2-4 1-5 0l-7-5-6 1-6-4z" fill="none" stroke="#111" stroke-width="2.4" stroke-linejoin="round"/><path d="M19 13l-5 5c2 2 4 1 6-1l4 2" fill="none" stroke="#111" stroke-width="2"/></svg></div>
    <div class="label">Initial face to face</div>
    <p class="desc">This is where we get more in depth about your project and talk about how we can help you.</p>
  </div>
  <div class="step col-3 row-1">
    <div class="icon"></div>
    <div class="label">1st base price estimate</div>
    <p class="desc">At this stage we will provide you with your first initial estimate based on our discussions, so we can deliver you the best possible product for your budget.</p>
  </div>

  <!-- Preliminary phase -->
  <div class="step col-1 row-2">
    <div class="icon"><svg viewBox="0 0 42 38"><rect x="9" y="4" width="20" height="28" fill="none" stroke="#111" stroke-width="2.4"/><path d="M13 11h12M13 16h12M13 21h7" stroke="#111" stroke-width="2"/><path d="M22 30l12-14 3 3-12 14-4 1z" fill="#111"/></svg></div>
    <div class="label">Preliminary agreement</div>
    <p class="desc">This is usually by phone or email, a quick chat with our builder, then a short questionnaire for you to fill out to see if we're a match to work together.</p>
  </div>
  <div class="step col-2 row-2">
    <div class="icon"><svg viewBox="0 0 42 38"><path d="M4 8h34M4 30h34M8 8v22M16 8v22M24 8v22M32 8l6 22" fill="none" stroke="#111" stroke-width="2"/></svg></div>
    <div class="label">Concept drawings</div>
    <p class="desc">This is where we get more in depth about your project and talk about how we can help you.</p>
  </div>
  <div class="step col-3 row-2">
    <div class="icon"><svg viewBox="0 0 42 38"><rect x="4" y="7" width="34" height="24" fill="none" stroke="#111" stroke-width="2.2"/><rect x="9" y="12" width="12" height="14" fill="none" stroke="#111" stroke-width="1.8"/><path d="M25 13h9M25 18h9M25 23h6" stroke="#111" stroke-width="1.8"/></svg></div>
    <div class="label">Updated estimate</div>
    <p class="desc">At this stage we will provide you with your first initial estimate based on our discussions, so we can deliver you the best possible product for your budget.</p>
  </div>

  <div class="step col-1 row-3">
    <div class="icon"><svg viewBox="0 0 42 38"><rect x="5" y="8" width="18" height="24" transform="rotate(-14 14 20)" fill="none" stroke="#111" stroke-width="2.2"/><rect x="15" y="5" width="18" height="24" fill="#fff" stroke="#111" stroke-width="2.2"/><path d="M19 11h10M19 16h10M19 21h6" stroke="#111" stroke-width="1.8"/><path d="M26 32l10-12 3 3-10 12-4 1z" fill="#111"/></svg></div>
    <div class="label">Sign contract</div>
    <p class="desc">This is usually by phone or email, a quick chat with our builder, then a short questionnaire for you to fill out to see if we're a match to work together.</p>
  </div>
  <div class="step col-2 row-3">
    <div class="icon"><svg viewBox="0 0 42 38"><g fill="none" stroke="#111" stroke-width="2"><rect x="8" y="6" width="8" height="26" transform="rotate(-30 12 32)"/><rect x="14" y="6" width="8" height="26" transform="rotate(-10 18 32)"/><rect x="20" y="6" width="8" height="26" transform="rotate(12 24 32)"/></g><path d="M21 10h6M21 15h6M21 20h6" stroke="#111" stroke-width="1.6"/></svg></div>
    <div class="label">Color selections</div>
    <p class="desc">This is where we get more in depth about your project and talk about how we can help you.</p>
  </div>
  <div class="step col-3 row-3">
    <div class="icon"><svg viewBox="0 0 42 38"><rect x="3" y="6" width="36" height="26" fill="none" stroke="#111" stroke-width="2.2"/><path d="M8 11h14v16H8zM15 11v8h7M26 12h9M26 17h9M26 22h9" fill="none" stroke="#111" stroke-width="1.6"/></svg></div>
    <div class="label">1st base plans estimate</div>
    <p class="desc">At this stage we will provide you with your first initial estimate based on our discussions, so we can deliver you the best possible product for your budget.</p>
  </div>

  <!-- Construction stage -->
  <div class="step col-1 row-4">
    <div class="icon"></div>
    <div class="label">Initial contact</div>
    <p class="desc">This is usually by phone or email, a quick chat with our builder, then a short questionnaire for you to fill out to see if we're a match to work together.</p>
  </div>
  <div class="step col-2 row-4">
    <div class="icon"></div>
    <div class="label">Initial face to face</div>
    <p class="desc">This is where we get more in depth about your project and talk about how we can help you.</p>
  </div>
  <div class="step col-3 row-4">
    <div class="icon"></div>
    <div class="label">1st base price estimate</div>
    <p class="desc">At this stage we will provide you with your first initial estimate based on our discussions, so we can deliver you the best possible product for your budget.</p>
  </div>
</div>
</body>
</html>
```